High Tech Real Estate Startup needs a business card

We are developing an innovative real estate marketing product based around advanced search and virtual reality.

We talk to people, we need business cards.

Target Market(s)

The target market is technology professionals and realtors.

Contact Information for Business Card

The information to be included will include

Name
Title
Phone Number
E-mail Address
www.quelzo.com

It should use simple iconography for each one of those fields.

Font styles to use
Other font styles liked:
• Co, Jubilat, Avenir

Colors

Designer to choose colors to be used in the design.

Requirements
Must have
• Clean aesthetic,
• Good use of negative space.
• It should use our company logo, shown in the attached file. It is able to use the negative of that logo (coloured font and white background) and I have attached other acceptable accent colours in a swatch file.
Should not have
• Should not be too busy
• No extraneous text (slogans, tag lines etc)

```html
<!DOCTYPE html>
<html lang="en">
<head>
<meta charset="utf-8">
<title>Quelzo business card</title>
<link rel="stylesheet" href="https://fonts.googleapis.com/css2?family=Lato:wght@300;400&display=swap">
<style>
  :root {
    --teal: #2cb5b9;
    --teal-dark: #1f9599;
    --paper: #ffffff;
    --backdrop: #e8e8e8;
    --ink: #3a3a3a;
  }
  * { margin: 0; padding: 0; box-sizing: border-box; }
  html, body { width: 1200px; height: 675px; overflow: hidden; }
  body {
    background: var(--backdrop);
    font-family: "Lato", Arial, sans-serif;
    position: relative;
  }
  .card {
    position: absolute;
    top: 189px;
    width: 520px;
    height: 297px;
    box-shadow: 0 2px 10px rgba(0,0,0,0.12);
    overflow: hidden;
  }
  /* Front */
  .card-front { left: 50px; background: var(--teal); }
  .frame {
    position: absolute;
    border: 1px solid rgba(255,255,255,0.75);
  }
  .frame-outer { left: 52px; top: 40px; width: 406px; height: 214px; }
  .frame-inner { left: 62px; top: 48px; width: 406px; height: 214px; }
  .brand-name {
    position: absolute;
    left: 0; right: 0; top: 50%;
    transform: translateY(-50%);
    text-align: center;
    color: var(--paper);
    font-weight: 400;
    font-size: 54px;
    letter-spacing: 5px;
  }
  /* Back */
  .card-back { left: 630px; background: var(--paper); }
  .band {
    position: absolute;
    top: 0; bottom: 0;
    width: 30px;
    background: var(--teal);
  }
  .band-left { left: 40px; }
  .band-right { right: 38px; }
  .band-label {
    position: absolute;
    left: 50%;
    color: var(--paper);
    font-size: 11px;
    letter-spacing: 0.5px;
    white-space: nowrap;
    transform-origin: center;
  }
  .band-left .band-label { top: 200px; transform: translateX(-50%) rotate(90deg); }
  .band-right .band-label { top: 70px; transform: translateX(-50%) rotate(90deg); }
  .contact-list {
    position: absolute;
    left: 148px;
    top: 82px;
    list-style: none;
  }
  .contact-item {
    display: flex;
    align-items: center;
    height: 33px;
    color: var(--ink);
    font-weight: 300;
    font-size: 17px;
  }
  .contact-icon {
    width: 26px; height: 26px;
    margin-right: 9px;
    flex: none;
  }
</style>
</head>
<body>

<section class="card card-front" aria-label="Card front">
  <div class="frame frame-outer"></div>
  <div class="frame frame-inner"></div>
  <div class="brand-name">QUELZO</div>
</section>

<section class="card card-back" aria-label="Card back">
  <div class="band band-left"><span class="band-label">QUELZO</span></div>
  <div class="band band-right"><span class="band-label">www.quelzo.com</span></div>

  <ul class="contact-list">
    <li class="contact-item">
      <svg class="contact-icon" viewBox="0 0 26 26" aria-hidden="true">
        <rect x="0.5" y="0.5" width="25" height="25" fill="none" stroke="#2cb5b9"/>
        <rect x="3" y="3" width="20" height="20" fill="#2cb5b9"/>
        <circle cx="13" cy="10.5" r="3.2" fill="#fff"/>
        <path d="M7 19 q6-7 12 0 z" fill="#fff"/>
      </svg>
      Your Name Here
    </li>
    <li class="contact-item">
      <svg class="contact-icon" viewBox="0 0 26 26" aria-hidden="true">
        <rect x="0.5" y="0.5" width="25" height="25" fill="none" stroke="#2cb5b9"/>
        <rect x="3" y="3" width="20" height="20" fill="#2cb5b9"/>
        <line x1="9" y1="9" x2="17" y2="17" stroke="#fff" stroke-width="2"/>
      </svg>
      Your Title
    </li>
    <li class="contact-item">
      <svg class="contact-icon" viewBox="0 0 26 26" aria-hidden="true">
        <rect x="0.5" y="0.5" width="25" height="25" fill="none" stroke="#2cb5b9"/>
        <rect x="3" y="3" width="20" height="20" fill="#2cb5b9"/>
        <rect x="7" y="9" width="12" height="8" fill="none" stroke="#fff" stroke-width="1.2"/>
        <path d="M7 9 l6 4.5 l6-4.5" fill="none" stroke="#fff" stroke-width="1.2"/>
      </svg>
      yourmail@email.com
    </li>
    <li class="contact-item">
      <svg class="contact-icon" viewBox="0 0 26 26" aria-hidden="true">
        <rect x="0.5" y="0.5" width="25" height="25" fill="none" stroke="#2cb5b9"/>
        <rect x="3" y="3" width="20" height="20" fill="#2cb5b9"/>
        <path d="M9.5 8 l2 0 l1 3 l-1.5 1 q1 2.5 3 3.5 l1-1.5 l3 1 l0 2 q-1 1.5-3 1 q-5-2-6.5-7 q-0.3-2 1-3z" fill="#fff"/>
      </svg>
      +(000) 123 456 789
    </li>
  </ul>
</section>

</body>
</html>
```